Need a cool, fun 4x9 rack card!

Hi we need a 4 x 9 rack card. We have two tours, one for each side. One side will be Bluffline Moped Tours which should be real fun depiction of riding scooters through Red Rock Canyon, and the other side will be Bluffline Outlook Tours which is our van tour option. Looking for something colorful, and super fun looking.

The pics with scooters in them are with Bluffline Moped Tours (one side)
The pics that don’t show scooters are for the other side.

You can be creative, resize, crop, whatever to make the rack card look cool and fun.

Emphasis on the top part of the card is good as that is what will show above the rack when customers walk by.

Thanks!

Target Market(s)

Vacationers in Las Vegas

Industry/Entity Type

Tours

Font styles to use
Sans Serif

Colors
FFC000
F8CF3A
FAE287
FDF2CF
FEFAEE

Requirements
Must have
• Great color, catchy design, and look like fun.
Nice to have
• Look like fun.
Should not have
• Be boring

```html
<!DOCTYPE html>
<html lang="en">
<head>
<meta charset="utf-8">
<title>Bluffline Tours Rack Cards</title>
<link rel="stylesheet" href="https://fonts.googleapis.com/css2?family=Bebas+Neue&family=Poppins:wght@400;600;700&display=swap">
<style>
  :root{
    --page:#e9e9e9;
    --rust:#b9552f;
    --rust-dark:#9a4025;
    --rust-light:#d8794f;
    --red:#c8321f;
    --peach-top:#f3c2ac;
    --peach-mid:#f9dfd2;
    --peach-low:#fdf3ee;
    --ink:#2b2522;
    --white:#ffffff;
  }
  *{box-sizing:border-box;margin:0;padding:0}
  html,body{width:720px;height:1200px;overflow:hidden;background:var(--page)}
  body{position:relative;font-family:'Poppins',sans-serif;color:var(--ink)}
  .rack-card{position:absolute;top:222px;width:336px;height:756px;overflow:hidden;
    background:linear-gradient(180deg,var(--peach-top) 0%,var(--peach-mid) 55%,var(--peach-low) 100%);
    box-shadow:0 4px 14px rgba(0,0,0,.25)}
  .rack-card--moped{left:16px}
  .rack-card--outlook{left:368px}
  .hero{position:absolute;left:0;top:0;width:336px;height:400px}
  .headline{position:absolute;left:0;width:100%;text-align:center;color:var(--white);
    text-shadow:0 2px 4px rgba(0,0,0,.35)}
  .headline__main{font-family:'Bebas Neue',sans-serif;font-size:50px;line-height:1;letter-spacing:.5px}
  .headline__sub{font-family:'Poppins',sans-serif;font-weight:700;font-size:17px;line-height:1.4;margin-top:4px}
  .photo{position:absolute;border-radius:50%;border:4px solid var(--white);
    box-shadow:0 2px 5px rgba(0,0,0,.2)}
  .brand-mark{position:absolute;left:19px;top:212px;width:86px;height:86px;border-radius:50%;
    background:var(--white);border:3px solid var(--rust-dark);display:flex;align-items:center;
    justify-content:center;text-align:center;font-weight:700;font-size:11px;line-height:1.25;color:var(--rust-dark);padding:8px}
  .quote{position:absolute;left:10px;color:var(--red);font-weight:700;font-size:12.5px;line-height:1.32}
  .features{position:absolute;left:14px;right:10px;list-style:none;font-size:11px;line-height:1.3}
  .features li{position:relative;padding-left:18px;margin-bottom:7px}
  .features li::before{content:"";position:absolute;left:3px;top:6px;width:4px;height:4px;border-radius:50%;background:var(--ink)}
  .scene{position:absolute;left:0;width:336px}
  .scene--scooters{top:612px;height:144px;
    background:linear-gradient(180deg,rgba(253,243,238,0) 0%,#d9cdbd 25%,#b9aa98 60%,#8f8375 100%)}
  .scene--van{top:572px;height:120px;
    background:linear-gradient(180deg,rgba(253,243,238,0) 0%,#c8a58e 20%,#8f6c5c 55%,#6a6f7d 100%);
    clip-path:polygon(0 0,100% 0,100% 88%,92% 84%,84% 92%,74% 86%,64% 94%,52% 87%,40% 95%,30% 86%,18% 93%,8% 86%,0 92%)}
  .footer{position:absolute;left:0;bottom:0;width:336px;height:66px;background:var(--white);
    display:flex;justify-content:space-between;padding:10px 14px 0 20px}
  .footer__label{color:var(--red);font-weight:700;font-size:10px}
  .footer__address{font-size:9px;line-height:1.3;margin-top:2px}
  .footer__phone{color:var(--red);font-weight:700;font-size:14px;line-height:1}
  .footer__email{font-size:9px;margin-top:4px}
  .footer__web{font-size:9px;color:var(--red);margin-top:3px}
</style>
</head>
<body>

<section class="rack-card rack-card--moped">
  <svg class="hero" viewBox="0 0 336 400" role="img" aria-label="Row of red and cream scooters parked before red rock mountains">
    <defs>
      <linearGradient id="moped-sky" x1="0" y1="0" x2="0" y2="1">
        <stop offset="0" stop-color="#cd6a44"/>
        <stop offset="0.5" stop-color="#b9552f"/>
        <stop offset="1" stop-color="#c97552"/>
      </linearGradient>
    </defs>
    <path d="M0 0H336V392C240 382 90 310 0 168Z" fill="url(#moped-sky)"/>
    <path d="M0 168C90 310 240 382 336 392" fill="none" stroke="#c8321f" stroke-width="5"/>
  </svg>
  <div class="headline" style="top:34px">
    <div class="headline__main">#1 RANKED TOUR</div>
    <div class="headline__sub">IN LAS VEGAS, TREKRATER</div>
  </div>
  <div class="brand-mark">Bluffline Moped Tours</div>
  <div class="photo" role="img" aria-label="Red dirt bike parked on pavers" style="left:206px;top:232px;width:106px;height:106px;background:radial-gradient(circle at 45% 55%,#c8321f 0 28%,#8a8a8a 29% 60%,#bdb6ad 61%)"></div>
  <div class="photo" role="img" aria-label="Riders on scooters below rugged red rock peaks" style="left:94px;top:266px;width:120px;height:120px;background:linear-gradient(180deg,#7aa6d6 0%,#a88a7c 38%,#8a6f61 60%,#c9b79c 80%,#7d8f5a 100%)"></div>
  <div class="photo" role="img" aria-label="Rider on a scooter beside a canyon trail sign" style="left:204px;top:310px;width:126px;height:126px;background:linear-gradient(180deg,#6c9fd4 0%,#9db9d8 30%,#a58c78 50%,#c9b79c 75%,#b8a98f 100%)"></div>
  <p class="quote" style="top:408px">“The most fun<br>thing we did&nbsp; in Vegas,<br>we’d recommend it to anyone!”</p>
  <ul class="features" style="top:464px">
    <li>Take fantastic pics and take home lifetime memories!</li>
    <li>No experience needed - we teach you!</li>
    <li>Learn about the fascinating history, geology, native people and animals of the gorgeous Mohave Desert</li>
    <li>About 4 hours from pickup to drop off</li>
    <li>Convenient pickup locations at or near your hotel!</li>
  </ul>
  <div class="scene scene--scooters" role="img" aria-label="Fleet of white, red and cream scooters lined up on a desert lot"></div>
</section>

<section class="rack-card rack-card--outlook">
  <svg class="hero" viewBox="0 0 336 400" role="img" aria-label="Traveler with arms outstretched sitting on red sandstone">
    <defs>
      <linearGradient id="outlook-sky" x1="0" y1="0" x2="0" y2="1">
        <stop offset="0" stop-color="#d27049"/>
        <stop offset="0.45" stop-color="#b24a2a"/>
        <stop offset="1" stop-color="#a94428"/>
      </linearGradient>
    </defs>
    <path d="M0 0H336V332C250 324 100 292 0 226Z" fill="url(#outlook-sky)"/>
    <path d="M0 226C100 292 250 324 336 332" fill="none" stroke="#c8321f" stroke-width="5"/>
  </svg>
  <div class="headline" style="top:34px">
    <div class="headline__main">#1 RATED VAN TOUR</div>
    <div class="headline__sub">IN THE RED ROCK CANYON,<br>TREKRATER</div>
  </div>
  <div class="photo" role="img" aria-label="Two smiling riders in helmets" style="left:216px;top:126px;width:114px;height:114px;background:linear-gradient(180deg,#b7553a 0%,#c8321f 35%,#d9a88c 60%,#3b3b3b 100%)"></div>
  <div class="photo" role="img" aria-label="Blue sky over open desert valley" style="left:136px;top:190px;width:100px;height:100px;background:linear-gradient(180deg,#4f86c6 0%,#8fb6de 50%,#7b8a8a 68%,#a79c86 100%)"></div>
  <div class="photo" role="img" aria-label="Fenced country road leading toward striped rock hills" style="left:220px;top:244px;width:110px;height:110px;background:linear-gradient(180deg,#5e95d0 0%,#a7c4e0 35%,#d7b59e 50%,#6c8c4e 70%,#c9c4ba 100%)"></div>
  <p class="quote" style="top:276px">“I learned so<br>much and had no<br>idea the outskirts of Las<br>Vegas were so gorgeous and so<br>steeped in old-west history!</p>
  <ul class="features" style="top:362px">
    <li>Take fantastic pics of some of the most gorgeous scenery in the world.</li>
    <li>Learn so much about the history of Las Vegas and the Red Rock Area</li>
    <li>See where natives roamed the lands and learn how they survived</li>
    <li>Walk through the historic Hollis Grant estate - Spring Mountain Ranch</li>
    <li>Stop and experience old-school small town Nevada with a hangout and snack break in the old mining town of Blue Diamond.</li>
    <li>See the “Real Las Vegas” and leave with an entirely new appreciation and perspective!</li>
  </ul>
  <div class="scene scene--van" role="img" aria-label="Group of guests posing beside a colorfully painted tour van"></div>
  <footer class="footer">
    <div>
      <div class="footer__label">Tour Starts at:</div>
      <div class="footer__address">2400 Sandstone Way<br>Las Vegas, NV . 89161</div>
    </div>
    <div>
      <div class="footer__phone">702-555-0148</div>
      <div class="footer__email">info@blufflinemopedtours.com</div>
      <div class="footer__web">www.blufflinemopedtours.com</div>
    </div>
  </footer>
</section>

</body>
</html>
```